Bright Lane Collective needs updated website.

Our current website was designed on wix.com. (www.brightlanecollective.example).
We would like something a little more customized for what our company offers. Bright Lane Collective is a company specializing in connecting consumers with trustworthy and affordable service professionals. We need the website to be approachable and easy to use, while conveying our "Bright Lane" reputation.
Reason: Our project is now guaranteed. Please send your ideas. Thank you!
Target Market(s)
Homeowners
Industry/Entity Type
It Company
Look and feel

```html
<!DOCTYPE html>
<html lang="en">
<head>
<meta charset="utf-8">
<title>Bright Lane Collective</title>
<link href="https://fonts.googleapis.com/css2?family=Arimo:wght@400;700&family=Source+Sans+3:wght@400;600&display=swap" rel="stylesheet">
<style>
  :root {
    --brand-blue: #1f7fd6;
    --brand-navy: #0d3f8f;
    --button-blue: #1a77c0;
    --ink: #111111;
    --footer-bg: #4a4a4a;
    --footer-text: #eeeeee;
    --rule: #9a9a9a;
    --white: #ffffff;
  }
  * { margin: 0; padding: 0; box-sizing: border-box; }
  html, body { width: 899px; height: 1200px; overflow: hidden; background: var(--white); }
  body { position: relative; font-family: "Arimo", Arial, sans-serif; color: var(--ink); }

  .site-header {
    position: absolute; left: 0; top: 0; width: 899px; height: 80px;
    background: var(--brand-blue); border-bottom: 3px solid var(--brand-navy);
  }
  .brand { position: absolute; left: 46px; top: 15px; display: flex; align-items: center; gap: 10px; }
  .brand-dot { width: 48px; height: 48px; border-radius: 50%; background: var(--white); }
  .brand-name { font-family: "Source Sans 3", sans-serif; font-weight: 600; font-size: 24px; color: var(--white); }

  .main-nav { position: absolute; right: 44px; top: 0; height: 77px; display: flex; align-items: center; }
  .main-nav a {
    display: flex; align-items: center; height: 77px; padding: 0 12px;
    font-size: 14px; color: var(--white); text-decoration: none; position: relative;
  }
  .main-nav a + a::before {
    content: ""; position: absolute; left: 0; top: 38px; width: 1px; height: 7px; background: rgba(0,0,0,0.35);
  }
  .main-nav a.is-active { background: var(--white); color: var(--brand-blue); }

  .hero {
    position: absolute; left: 0; top: 80px; width: 899px; height: 499px;
    border-bottom: 4px solid var(--brand-navy);
    background: linear-gradient(100deg, #d9d7d2 0%, #ecebe8 35%, #c9c9cc 60%, #5a5f6a 78%, #3b4660 100%);
  }
  .hero-arrow {
    position: absolute; width: 77px; height: 77px; border-radius: 50%;
    background: rgba(190,190,190,0.85); display: flex; align-items: center; justify-content: center;
  }
  .hero-arrow--prev { left: 16px; top: 195px; }
  .hero-arrow--next { left: 795px; top: 205px; }
  .hero-dots { position: absolute; left: 407px; top: 455px; display: flex; gap: 3px; }
  .hero-dots span { width: 29px; height: 29px; border-radius: 50%; background: rgba(170,170,170,0.9); }

  .photo { position: absolute; }
  .photo--agent { left: 4px; top: 581px; width: 262px; height: 262px; background: linear-gradient(160deg, #e9e4dd, #c9a98a 55%, #2b2f3a); }
  .photo--technician { left: 646px; top: 845px; width: 253px; height: 268px; background: linear-gradient(170deg, #d7d9dc, #9ea3a8 50%, #2a2c33); }

  .section-title { position: absolute; font-weight: 700; font-size: 23px; letter-spacing: 0.2px; }
  .section-copy { position: absolute; font-size: 16px; line-height: 20px; }
  .btn-read-more {
    position: absolute; width: 128px; height: 30px; background: var(--button-blue); color: var(--white);
    font-family: "Source Sans 3", sans-serif; font-weight: 600; font-size: 19px;
    display: flex; align-items: center; justify-content: center; text-decoration: none;
  }

  .intro-title { left: 347px; top: 615px; }
  .intro-copy { left: 300px; top: 657px; width: 525px; }
  .intro-btn { left: 300px; top: 794px; }

  .section-rule { position: absolute; left: 4px; top: 844px; width: 642px; height: 1px; background: var(--rule); }

  .feature-title { left: 46px; top: 882px; font-size: 24px; }
  .feature-copy { left: 46px; top: 925px; width: 590px; font-size: 15.5px; }
  .feature-btn { left: 46px; top: 1061px; }

  .site-footer {
    position: absolute; left: 0; top: 1114px; width: 899px; height: 86px; background: var(--footer-bg);
    font-family: "Source Sans 3", sans-serif; color: var(--footer-text); font-size: 17px;
  }
  .footer-nav a { position: absolute; top: 14px; color: var(--footer-text); text-decoration: none; }
  .footer-legal { position: absolute; left: 0; top: 54px; width: 899px; text-align: center; }
  .footer-legal .sep { margin: 0 10px; }
</style>
</head>
<body>
  <header class="site-header">
    <div class="brand">
      <span class="brand-dot"></span>
      <span class="brand-name">Bright Lane Collective</span>
    </div>
    <nav class="main-nav">
      <a href="#" class="is-active">HOME</a>
      <a href="#">SERVICIES</a>
      <a href="#">ABOUT US</a>
      <a href="#">CONTACT</a>
    </nav>
  </header>

  <section class="hero" role="img" aria-label="Plumber repairing pipes under a bathtub with a toolbox beside him">
    <span class="hero-arrow hero-arrow--prev">
      <svg width="30" height="30" viewBox="0 0 30 30"><polyline points="24,6 6,15 24,24" fill="none" stroke="#333" stroke-width="2.5"/></svg>
    </span>
    <span class="hero-arrow hero-arrow--next">
      <svg width="30" height="30" viewBox="0 0 30 30"><polyline points="6,6 24,15 6,24" fill="none" stroke="#333" stroke-width="2.5"/></svg>
    </span>
    <div class="hero-dots"><span></span><span></span><span></span><span></span></div>
  </section>

  <div class="photo photo--agent" role="img" aria-label="Smiling customer service agent wearing a headset"></div>
  <h2 class="section-title intro-title">YOU CAN COUNT ON US</h2>
  <p class="section-copy intro-copy">Sometimes things are just easier when you know someone in the business. That's where Bright Lane Collective comes in. &nbsp;Whether your Air Conditioner is on the fritz, you've got a leaky roof, or need &nbsp;a car salesman you can actually trust.. &nbsp;Whatever it is, we connect you with Saint Louis' most reputable and affordable solutions, all at NO COST TO YOU!!</p>
  <a href="#" class="btn-read-more intro-btn">Read More</a>

  <div class="section-rule"></div>

  <h2 class="section-title feature-title">ANOTHER TITLE</h2>
  <p class="section-copy feature-copy">Lorem ipsum dolor sit amet, consectetur adipisicing elit, sed do eiusmod tempor incididunt ut labore et dolore magna aliqua. Ut enim ad minim veniam, quis nostrud exercitation ullamco laboris nisi ut aliquip ex ea commodo consequat. Duis aute irure dolor in reprehenderit in voluptate velit esse cillum dolore eu fugiat nulla pariatur. Excepteur sint occaecat cupidatat non proident, sunt in culpa qui officia deserunt mollit anim id est laborum</p>
  <a href="#" class="btn-read-more feature-btn">Read More</a>
  <div class="photo photo--technician" role="img" aria-label="HVAC technician in a hard hat giving a thumbs up beside an air conditioning unit"></div>

  <footer class="site-footer">
    <nav class="footer-nav">
      <a href="#" style="left:234px; top:13px;">Home</a>
      <a href="#" style="left:329px;">Services</a>
      <a href="#" style="left:438px;">About Us</a>
      <a href="#" style="left:551px;">Contact</a>
    </nav>
    <p class="footer-legal">Copyright Bright Lane Company<span class="sep">|</span>Terms and Conditions<span class="sep">|</span>Contact</p>
  </footer>
</body>
</html>
```